Northwind Crate Traders Needs a FRESH website

We would like a creative minded designer to take on the task to Re-design our website. Its a simple 5-7 pages. With no cart, no complex html. Just plain information about our company and products we import and export. Pictures added to the product section. Since Our logo its Blue, we would like the designer to use complementing colors in order to make the website look cleaner and modern.

Target Market(s)

The target audience will be companies looking to purchase plastic related products. Companies looking to purchase large quantities of plastic containers (Shampoo bottles, caps, sprayers, mist sprayers, cosmetic containers etc).

Industry/Entity Type

It Company

Font styles to use
Sans Serif

Requirements
Must have
• We have a section in which we would like to add pictures of some of the products we carry, therefore having an easy and clean way to navigate through the pictures will be a plus.

```html
<!DOCTYPE html>
<html lang="en">
<head>
<meta charset="utf-8">
<title>Northwind Crate Traders</title>
<link href="https://fonts.googleapis.com/css2?family=Open+Sans:wght@400;600;700&display=swap" rel="stylesheet">
<style>
:root{
  --blue:#1479cf;
  --blue-deep:#0a6cc4;
  --blue-band:#0b72c9;
  --blue-dark:#095aa3;
  --blue-light:#2b8ede;
  --ink:#333a40;
  --grey:#8a8f94;
  --line:#dcdfe2;
  --paper:#f7f7f7;
  --white:#ffffff;
}
*{margin:0;padding:0;box-sizing:border-box}
html,body{width:1200px;height:3061px;overflow:hidden}
body{font-family:"Open Sans",Verdana,sans-serif;color:var(--ink);background:var(--white);position:relative}
.abs{position:absolute}
a{color:inherit;text-decoration:none}

/* top bar */
.topbar{left:0;top:0;width:1200px;height:73px;background:var(--blue)}
.social{display:flex;gap:6px}
.social span{width:24px;height:24px;border-radius:50%;background:var(--white);display:block}
.topbar .social{left:836px;top:24px}
.search{left:941px;top:22px;width:212px;height:27px;border-radius:14px;background:var(--white);font-size:12px;color:#9aa0a6;padding:5px 14px}

/* header */
.header{left:0;top:73px;width:1200px;height:139px;background:var(--white);box-shadow:0 2px 6px rgba(0,0,0,.08)}
.brand{left:82px;top:20px;width:214px;height:175px;text-align:center}
.brand .mark{width:96px;height:96px;border-radius:50%;background:var(--blue);margin:0 auto 8px;border:6px solid var(--white)}
.brand .name{font-size:24px;font-weight:700;line-height:1.1;color:var(--blue)}
.nav{top:136px;font-size:14px;letter-spacing:.5px;color:#555b60}

/* hero */
.hero{left:0;top:212px;width:1200px;height:478px;background:linear-gradient(180deg,#f4f4f4,#e9eaeb)}
.hero h1{left:127px;top:308px;font-size:25px;font-weight:700;color:var(--blue);letter-spacing:.5px}
.hero .lead{left:131px;top:348px;width:500px;font-size:25px;line-height:31px;color:#3a3f44}
.hero .copy{left:131px;top:420px;width:490px;font-size:15px;line-height:23px;color:#92979c}
.btn{display:flex;align-items:center;justify-content:center;border-radius:9px;font-size:12px;color:var(--white)}
.btn-dark{background:var(--blue-deep);border-bottom:3px solid var(--blue-dark)}
.btn-light{background:#2d9ae0;border-bottom:3px solid #1a7cc0}
.globe{left:735px;top:261px;width:465px;height:429px;background:radial-gradient(circle at 40% 35%,#bfe4fb 0,#4aa4e6 28%,#d9c2ae 62%,rgba(233,234,235,0) 78%)}

/* section titles */
.section-title{font-size:19px;font-weight:600;color:#555b60}
.section-title b{color:var(--blue);font-weight:700}
.rule{height:2px;background:var(--line)}
.rule::before{content:"";position:absolute;left:0;top:-2px;width:62px;height:6px;background:var(--blue)}
.dots{display:flex;gap:4px}
.dots i{width:10px;height:10px;border-radius:50%;background:#b5b9bd;display:block}
.dots i:first-child{background:var(--blue)}

/* products */
.products{left:0;top:690px;width:1200px;height:796px;background:var(--white)}
.card{width:249px;height:163px;border:4px solid #d3d5d7;background:var(--white);padding:6px}
.card .photo{width:100%;height:100%}
.card .ribbon{position:absolute;right:-10px;top:-4px;width:62px;height:26px;background:var(--blue);transform:rotate(45deg) translate(10px,2px)}
.label{width:249px;text-align:center;font-size:16px;color:var(--blue)}
.view-other{left:489px;top:1371px;width:222px;height:41px;border-radius:12px;font-size:13px;letter-spacing:.5px}

/* welcome + offer */
.band{left:0;top:1486px;width:1200px;height:604px;background:var(--blue-band)}
.band h2{font-size:18px;font-weight:700;color:var(--white)}
.band .line{height:2px;background:rgba(255,255,255,.25)}
.band .line::before{content:"";position:absolute;left:0;top:-2px;width:62px;height:5px;background:#6fb7ee}
.welcome{left:102px;top:1652px;width:490px;font-size:15.5px;line-height:22.5px;color:var(--white)}
.welcome p+p{margin-top:22px}
.offer{left:647px;width:440px;display:flex;gap:20px}
.offer .icon{width:84px;height:72px;border-radius:5px;background:linear-gradient(#fdfdfd,#dcdfe2);border-bottom:4px solid #a9afb5;flex:none;display:flex;align-items:center;justify-content:center}
.offer h3{font-size:15px;font-weight:400;color:var(--white);letter-spacing:.5px;margin-top:6px}
.offer p{font-size:13px;line-height:19px;color:#e3f0fb;margin-top:2px}
.band .dots i{background:#8cc2ee}
.band .dots i:first-child{background:var(--white)}

/* news */
.news{left:0;top:2090px;width:1200px;height:531px;background:var(--paper)}
.news-photo{left:88px;top:2245px;width:314px;height:204px;border:4px solid #d3d5d7;background:linear-gradient(180deg,#e3d6b8 0,#c9c4b4 35%,#5e6c7c 55%,#a44b3a 75%,#356e9a 100%)}
.btn-flat{height:36px;font-size:13px;color:var(--white);display:flex;align-items:center;justify-content:center}
.article{width:310px;display:flex;gap:10px}
.article h4{font-size:14px;font-weight:400;color:var(--blue-deep);letter-spacing:.3px}
.article p{font-size:13px;line-height:20px;color:#8b9095;margin-top:2px}
.article a{font-size:13px;color:var(--blue-deep)}

/* footer */
.footer{left:0;top:2621px;width:1200px;height:396px;background:var(--blue)}
.footer-top{left:0;top:2621px;width:1200px;height:43px;background:var(--blue-light)}
.footer h5{font-size:16px;font-weight:600;color:var(--white);letter-spacing:.5px}
.links{width:178px;list-style:none}
.links li{font-size:15px;color:var(--white);height:35px;border-bottom:1px solid rgba(255,255,255,.18);display:flex;align-items:center;letter-spacing:.5px}
.links li::before{content:"›";font-weight:700;font-size:20px;margin-right:6px;line-height:1}
.email{left:647px;top:2806px;width:186px;height:31px;background:var(--white);font-size:12px;color:#777;padding:7px 10px}
.submit{left:649px;top:2851px;width:121px;height:29px;background:var(--blue-dark);color:var(--white);font-size:12px;display:flex;align-items:center;justify-content:center;letter-spacing:.5px}
.foot-brand{left:900px;top:2715px;width:200px;text-align:center}
.foot-brand .mark{width:76px;height:76px;border-radius:50%;background:var(--white);margin:0 auto 10px}
.foot-brand .name{font-size:22px;font-weight:700;line-height:1.15;color:var(--white)}
.footer .social{left:954px;top:2867px}
.bottombar{left:0;top:3017px;width:1200px;height:44px;background:var(--blue-deep);font-size:12px;color:var(--white)}
</style>
</head>
<body>

<!-- top bar -->
<div class="abs topbar"></div>
<div class="abs social" aria-label="Social links"><span></span><span></span><span></span></div>
<div class="abs search">Keyword Search...</div>

<!-- header -->
<header class="abs header"></header>
<div class="abs brand">
  <div class="mark"></div>
  <div class="name">Northwind Crate Traders</div>
</div>
<nav>
  <a class="abs nav" style="left:400px">HOME</a>
  <a class="abs nav" style="left:512px">WHO WE ARE</a>
  <a class="abs nav" style="left:676px">WHAT WE OFFER</a>
  <a class="abs nav" style="left:861px">MARKETS WE SERVE</a>
  <a class="abs nav" style="left:1069px">CONTACT</a>
</nav>

<!-- hero -->
<section class="abs hero"></section>
<div class="abs globe" role="img" aria-label="Open hands holding a glowing blue globe"></div>
<h1 class="abs hero-title" style="left:127px;top:308px;font-size:25px;font-weight:700;color:var(--blue);letter-spacing:.5px">YOU DREAM IT&nbsp; AND WE DELIVER IT</h1>
<p class="abs" style="left:131px;top:348px;width:500px;font-size:25px;line-height:31px;color:#3a3f44">Lorem ipsum dolor sit amet consec tetur adipiscing elit sed non odio lorem felis</p>
<p class="abs" style="left:131px;top:420px;width:490px;font-size:15px;line-height:23px;color:#92979c">Lorem ipsum dolor sit amet, consectetur adipiscing elit. Sed non odio lorem. Pellentesque nec lacinia felis. Morbi sed est posuere orci faucibus feugiat a vitae quam.</p>
<a class="abs btn btn-dark" style="left:131px;top:512px;width:130px;height:35px">More details +</a>
<a class="abs btn btn-light" style="left:278px;top:512px;width:128px;height:35px">Contact us ✉</a>

<!-- products -->
<section class="abs products"></section>
<h2 class="abs section-title" style="left:92px;top:745px">Our <b>Products</b></h2>
<div class="abs rule" style="left:94px;top:793px;width:998px"></div>
<div class="abs dots" style="left:1042px;top:772px"><i></i><i></i><i></i></div>

<div class="abs card" style="left:169px;top:855px"><div class="photo" role="img" aria-label="Blue plastic bottle caps" style="background:linear-gradient(135deg,#e9eef8,#3a5fd0 55%,#1f3aa8)"></div><span class="ribbon"></span></div>
<div class="abs label" style="left:169px;top:1029px">Plastic Caps</div>
<div class="abs card" style="left:476px;top:855px"><div class="photo" role="img" aria-label="Clear PET bottles" style="background:linear-gradient(90deg,#fff,#dfe5ea 50%,#fff)"></div></div>
<div class="abs label" style="left:476px;top:1029px">P.E.T Containers</div>
<div class="abs card" style="left:782px;top:855px"><div class="photo" role="img" aria-label="Light blue plastic storage crate" style="background:linear-gradient(180deg,#fff 5%,#8ccdf3 30%,#5bb6ee 90%,#fff)"></div></div>
<div class="abs label" style="left:782px;top:1029px">P.E./P.P. CONTAINERS</div>

<div class="abs card" style="left:169px;top:1112px"><div class="photo" role="img" aria-label="White and blue trigger sprayer" style="background:linear-gradient(135deg,#fff 15%,#e6e8ec 40%,#2c3fb0 75%,#fff)"></div></div>
<div class="abs label" style="left:169px;top:1284px">Sprayers</div>
<div class="abs card" style="left:476px;top:1112px"><div class="photo" role="img" aria-label="Steel injection molds" style="background:linear-gradient(90deg,#fff 10%,#9aa1a8 35%,#c3c8cc 55%,#8d949b 75%,#fff 90%)"></div></div>
<div class="abs label" style="left:476px;top:1284px">Molds</div>
<div class="abs card" style="left:782px;top:1112px"><div class="photo" role="img" aria-label="White plastic jars" style="background:linear-gradient(180deg,#fff,#f1ede2 50%,#fff)"></div></div>
<div class="abs label" style="left:782px;top:1284px">Jars</div>

<a class="abs btn btn-light view-other">VIEW OTHER PRODUCTS</a>

<!-- welcome + what we offer -->
<section class="abs band"></section>
<h2 class="abs" style="left:92px;top:1558px">Welcome to Northwind Crate Traders</h2>
<div class="abs line" style="left:92px;top:1607px;width:502px"></div>
<div class="abs welcome">
  <p>Northwind Crate Traders will be your first and last stop for sourcing products from all over the world, specifically Asia and South America.<br>We have partners all around the globe that helps us make the best decision in sourcing a product from and to any market.<br>Northwind Crate Traders will always make the right choice for our clients when dealing with factories all over the world.</p>
  <p>We at Northwind Crate Traders have a great relationship with our suppliers which leads us to become more efficient at sourcing products and delivering it to our clients.</p>
</div>
<h2 class="abs" style="left:633px;top:1558px">What we offer</h2>
<div class="abs line" style="left:633px;top:1607px;width:499px"></div>
<div class="abs dots" style="left:1043px;top:1580px"><i></i><i></i><i></i></div>

<div class="abs offer" style="top:1649px">
  <div class="icon"><svg width="40" height="40" viewBox="0 0 40 40" fill="none" stroke="#1479cf" stroke-width="4"><circle cx="16" cy="16" r="10"/><path d="M24 24l11 11" stroke-linecap="round"/></svg></div>
  <div><h3>PRODUCT RESEARCH</h3><p>Lorem ipsum dolor sit amet con sectetur adip iscing elit. Sed non</p></div>
</div>
<div class="abs offer" style="top:1745px">
  <div class="icon"><svg width="46" height="38" viewBox="0 0 46 38" fill="none" stroke="#1479cf" stroke-width="3"><rect x="3" y="6" width="25" height="20" rx="2"/><path d="M28 12h8l7 8v6H28z"/><circle cx="12" cy="30" r="4" fill="#fff"/><circle cx="35" cy="30" r="4" fill="#fff"/></svg></div>
  <div><h3>DELIVERY</h3><p>Lorem ipsum dolor sit amet con sectetur adip iscing elit. Sed non</p></div>
</div>
<div class="abs offer" style="top:1843px">
  <div class="icon"><svg width="44" height="36" viewBox="0 0 44 36" fill="#1479cf"><path d="M4 16l8 2 10-10 4 1-6 11 10 2 4-4 3 1-3 7 3 7-3 1-4-4-10 2 6 11-4 1-10-10-8 2z" transform="scale(.95)"/></svg></div>
  <div><h3>FREIGHT FORWARDING</h3><p>Lorem ipsum dolor sit amet con sectetur adip iscing elit. Sed non</p></div>
</div>
<div class="abs offer" style="top:1939px">
  <div class="icon"><svg width="38" height="38" viewBox="0 0 38 38" fill="none" stroke="#1479cf" stroke-width="3" stroke-linejoin="round"><path d="M19 3l15 7v18l-15 7-15-7V10z"/><path d="M4 10l15 7 15-7M19 17v18"/></svg></div>
  <div><h3>PACKAGING</h3><p>Lorem ipsum dolor sit amet con sectetur adip iscing elit. Sed non</p></div>
</div>

<!-- news -->
<section class="abs news"></section>
<h2 class="abs section-title" style="left:92px;top:2149px">News <b>Update</b></h2>
<div class="abs rule" style="left:94px;top:2199px;width:998px"></div>
<div class="abs news-photo" role="img" aria-label="Container port with stacked shipping containers and cranes"></div>
<a class="abs btn-flat" style="left:88px;top:2466px;width:168px;background:var(--blue-deep)">VIEW ALL ARTICLES</a>
<a class="abs btn-flat" style="left:265px;top:2466px;width:137px;background:#4a4d50;border-bottom:3px solid #2e3032">CONTACT US</a>
<div class="abs" style="left:743px;top:2220px;width:1px;height:356px;background:var(--line)"></div>
<div class="abs" style="left:420px;top:2378px;width:650px;height:1px;background:var(--line)"></div>
<div class="abs" style="left:88px;top:2541px;width:980px;height:1px;background:#cfd3d6"></div>

<div class="abs article" style="left:435px;top:2255px">
  <svg width="28" height="30" viewBox="0 0 28 30" fill="none" stroke="#1479cf" stroke-width="2"><path d="M3 2h14l5 5v20H3z"/><path d="M7 10h10M7 15h10M7 20h6"/><path d="M16 26l9-9 3 3-9 9h-3z" fill="#fff"/></svg>
  <div><h4>TITLE OF THE ARTICLE GOES HERE</h4><p>Lorem ipsum dolor sit amet, consecte-tur adipiscing elit. Phasellus tincidunt tellus leo, sodales vestibulum urna.</p><a>Read more →</a></div>
</div>
<div class="abs article" style="left:767px;top:2255px">
  <svg width="28" height="30" viewBox="0 0 28 30" fill="none" stroke="#1479cf" stroke-width="2"><path d="M3 2h14l5 5v20H3z"/><path d="M7 10h10M7 15h10M7 20h6"/><path d="M16 26l9-9 3 3-9 9h-3z" fill="#fff"/></svg>
  <div><h4>TITLE OF THE ARTICLE GOES HERE</h4><p>Lorem ipsum dolor sit amet, consecte-tur adipiscing elit. Phasellus tincidunt tellus leo, sodales vestibulum urna.</p><a>Read more →</a></div>
</div>
<div class="abs article" style="left:435px;top:2398px">
  <svg width="28" height="30" viewBox="0 0 28 30" fill="none" stroke="#1479cf" stroke-width="2"><path d="M3 2h14l5 5v20H3z"/><path d="M7 10h10M7 15h10M7 20h6"/><path d="M16 26l9-9 3 3-9 9h-3z" fill="#fff"/></svg>
  <div><h4>TITLE OF THE ARTICLE GOES HERE</h4><p>Lorem ipsum dolor sit amet, consecte-tur adipiscing elit. Phasellus tincidunt tellus leo, sodales vestibulum urna.</p><a>Read more →</a></div>
</div>
<div class="abs article" style="left:767px;top:2398px">
  <svg width="28" height="30" viewBox="0 0 28 30" fill="none" stroke="#1479cf" stroke-width="2"><path d="M3 2h14l5 5v20H3z"/><path d="M7 10h10M7 15h10M7 20h6"/><path d="M16 26l9-9 3 3-9 9h-3z" fill="#fff"/></svg>
  <div><h4>TITLE OF THE ARTICLE GOES HERE</h4><p>Lorem ipsum dolor sit amet, consecte-tur adipiscing elit. Phasellus tincidunt tellus leo, sodales vestibulum urna.</p><a>Read more →</a></div>
</div>

<!-- footer -->
<footer class="abs footer"></footer>
<div class="abs footer-top"></div>
<h5 class="abs" style="left:133px;top:2710px">Who we are</h5>
<ul class="abs links" style="left:133px;top:2768px"><li>Sublink here</li><li>Sublink here</li><li>Sublink here</li><li>Sublink here</li></ul>
<h5 class="abs" style="left:392px;top:2710px">What we offer</h5>
<ul class="abs links" style="left:392px;top:2768px"><li>Sublink here</li><li>Sublink here</li><li>Sublink here</li><li>Sublink here</li></ul>
<h5 class="abs" style="left:647px;top:2710px">Newsletter Signup</h5>
<p class="abs" style="left:647px;top:2776px;font-size:13px;color:var(--white)">Subscribe to get updates</p>
<div class="abs email">Email address</div>
<div class="abs submit">SUBMIT</div>
<div class="abs foot-brand">
  <div class="mark"></div>
  <div class="name">Northwind Crate Traders</div>
</div>
<div class="abs social" aria-label="Social links"><span></span><span></span><span></span></div>

<div class="abs bottombar"></div>
<p class="abs" style="left:128px;top:3031px;font-size:12px;color:var(--white)">Copyright © 2014 Northwind Crate Traders</p>
<p class="abs" style="left:906px;top:3031px;font-size:12px;color:var(--white)">FAQ &nbsp;·&nbsp; Sitemap &nbsp;·&nbsp; Privacy Policy</p>

</body>
</html>
```